Fancy looking Inspection Postcard

Postcard needed for customers to inspect their product once it is delivered. We'll be giving them the steps for inspecting their product and to contact us if any issues arise. Would like to see something that sticks out but uses our company's colors. Would like to see creativity. Possibly utilizing the diamond steel background like we have in our logo.

Target Market(s)

Customers of our manufacturing shop

Industry/Entity Type

Manufacturing - metal wall art, custom products

Requirements
Must have
• our colors and logo
Nice to have
• get creative. i like creativity

```html
<!DOCTYPE html>
<html lang="en">
<head>
<meta charset="utf-8">
<title>Customer Inspection Checklist Postcard</title>
<link rel="stylesheet" href="https://fonts.googleapis.com/css2?family=Oswald:wght@400;500;700&family=Roboto+Condensed:ital,wght@0,400;0,500;1,300;1,400;1,700&display=swap">
<style>
  :root {
    --page: #ffffff;
    --plate: #0b0b0b;
    --plate-hi: #1c1c1c;
    --yellow: #fdec00;
    --olive: #d9d523;
    --lime: #bcd637;
    --green: #98c454;
    --brand-green: #7bb342;
    --ink: #111111;
    --white: #ffffff;
  }
  * { box-sizing: border-box; margin: 0; padding: 0; }
  html, body { width: 748px; height: 1200px; overflow: hidden; background: var(--page); }
  .postcard {
    position: absolute; left: 24px; top: 409px; width: 700px; height: 382px;
    background: var(--plate); overflow: hidden;
    box-shadow: 0 1px 3px rgba(0,0,0,.25);
  }
  .postcard__plate {
    position: absolute; inset: 0 0 76px 0;
    background: radial-gradient(ellipse at 50% 40%, var(--plate-hi), var(--plate) 75%);
  }
  .postcard__title {
    position: absolute; top: 16px; left: 0; right: 0; text-align: center;
    font: 700 30px/1 "Oswald", sans-serif; letter-spacing: 1.5px; color: var(--white);
    display: flex; justify-content: center; align-items: center; gap: 12px;
  }
  .postcard__title .accent { color: var(--yellow); }
  .postcard__title svg { width: 24px; height: 24px; }
  .step {
    position: absolute; top: 97px; height: 180px; border-radius: 9px;
    padding: 36px 10px 0 20px; color: var(--ink);
  }
  .step--general { left: 38px; width: 141px; background: var(--yellow); }
  .step--welds { left: 191px; width: 140px; background: var(--olive); padding-top: 34px; }
  .step--finish { left: 343px; width: 153px; background: var(--lime); }
  .step--function { left: 508px; width: 153px; background: var(--green); }
  .step__badge {
    position: absolute; top: -24px; left: 50%; transform: translateX(-50%);
    width: 44px; height: 52px;
  }
  .step__heading {
    font: 700 17px/1.05 "Oswald", sans-serif; letter-spacing: .8px;
    text-align: center; text-transform: uppercase; margin-bottom: 10px; margin-left: -8px;
  }
  .step--welds .step__heading { font-size: 15px; margin-bottom: 9px; }
  .step__list { list-style: none; }
  .step__item {
    position: relative; padding-left: 20px; margin-bottom: 9px;
    font: 400 12.5px/1.3 "Oswald", sans-serif; letter-spacing: .2px;
  }
  .step__item svg { position: absolute; left: 0; top: 3px; width: 11px; height: 11px; }
  .contact-band {
    position: absolute; left: 0; right: 0; bottom: 0; height: 76px; background: var(--white);
  }
  .contact-band__corner {
    position: absolute; left: 0; bottom: 0; width: 150px; height: 76px; background: var(--brand-green);
  }
  .brand-mark {
    position: absolute; left: 47px; top: 290px; width: 104px; height: 104px; border-radius: 50%;
    background: var(--plate); display: flex; align-items: center; justify-content: center;
    text-align: center; padding: 0 14px 14px;
    font: 700 13px/1.05 "Oswald", sans-serif; letter-spacing: .5px; color: var(--brand-green);
  }
  .contact-band__text {
    position: absolute; top: 13px; font: italic 300 12px/1.4 "Roboto Condensed", sans-serif;
    color: var(--ink); white-space: nowrap;
  }
  .contact-band__text--reach { left: 168px; }
  .contact-band__text--review { left: 405px; }
  .contact-band__divider {
    position: absolute; left: 387px; top: 16px; width: 1px; height: 46px; background: var(--brand-green);
  }
  .contact-band__ask { font-weight: 700; font-size: 14px; color: var(--brand-green); }
</style>
</head>
<body>
<svg width="0" height="0" style="position:absolute">
  <defs>
    <symbol id="tick-box" viewBox="0 0 12 12">
      <rect x="0.75" y="0.75" width="10.5" height="10.5" fill="none" stroke="currentColor" stroke-width="1.2"/>
      <path d="M2.8 6.2 L5 8.4 L9.4 3.2" fill="none" stroke="currentColor" stroke-width="1.5"/>
    </symbol>
    <symbol id="badge" viewBox="0 0 44 52">
      <path d="M3 4 Q22 -2 41 4 L41 26 Q40 42 22 51 Q4 42 3 26 Z" fill="#0b0b0b" stroke="#bcd637" stroke-width="2"/>
    </symbol>
  </defs>
</svg>

<article class="postcard">
  <div class="postcard__plate"></div>

  <h1 class="postcard__title">
    <span>CUSTOMER INSEPCTION</span>
    <svg viewBox="0 0 12 12" style="color:var(--yellow)"><use href="#tick-box"/></svg>
    <span class="accent">CHECKLIST</span>
  </h1>

  <section class="step step--general">
    <svg class="step__badge" viewBox="0 0 44 52"><use href="#badge"/>
      <g fill="none" stroke="#fff" stroke-width="1.3"><path d="M22 12 L26 19 L18 19 Z"/><rect x="13" y="22" width="7" height="7"/><circle cx="27" cy="25.5" r="3.8"/></g>
    </svg>
    <h2 class="step__heading">Inspect<br>General</h2>
    <ul class="step__list">
      <li class="step__item"><svg><use href="#tick-box"/></svg>Is it what you<br>expected?</li>
      <li class="step__item"><svg><use href="#tick-box"/></svg>Is it bent,<br>disoriented?</li>
    </ul>
  </section>

  <section class="step step--welds">
    <svg class="step__badge" viewBox="0 0 44 52"><use href="#badge"/>
      <g fill="none" stroke="#fff" stroke-width="1.3"><path d="M15 29 L27 17"/><path d="M27 17 L29 15"/><path d="M29 11 L30 14 M33 14 L30 15 M32 18 L30 16"/><path d="M12 31 L30 31"/></g>
    </svg>
    <h2 class="step__heading">Inspect the welds if there are any</h2>
    <ul class="step__list">
      <li class="step__item"><svg><use href="#tick-box"/></svg>Do they<br>look clean?</li>
      <li class="step__item"><svg><use href="#tick-box"/></svg>Are there<br>any gaps?</li>
    </ul>
  </section>

  <section class="step step--finish">
    <svg class="step__badge" viewBox="0 0 44 52"><use href="#badge"/>
      <g fill="none" stroke="#fff" stroke-width="1.3"><rect x="14" y="12" width="14" height="19" rx="1"/><rect x="18" y="10" width="6" height="3"/><path d="M17 18 H25 M17 22 H22 M17 26 H21"/><circle cx="28" cy="28" r="4.5"/><path d="M26 28 L27.5 29.5 L30 26.5"/></g>
    </svg>
    <h2 class="step__heading">Inspect<br>the Finish</h2>
    <ul class="step__list">
      <li class="step__item"><svg><use href="#tick-box"/></svg>Are there any<br>areas not finished?</li>
      <li class="step__item"><svg><use href="#tick-box"/></svg>Are the colors<br>what you expected?</li>
    </ul>
  </section>

  <section class="step step--function">
    <svg class="step__badge" viewBox="0 0 44 52"><use href="#badge"/>
      <g fill="none" stroke="#fff" stroke-width="1.3"><circle cx="22" cy="21" r="5"/><circle cx="22" cy="21" r="2"/><path d="M22 10 V14 M22 28 V32 M11 21 H15 M29 21 H33 M14 13 L17 16 M27 26 L30 29 M30 13 L27 16 M17 26 L14 29"/></g>
    </svg>
    <h2 class="step__heading">Check for<br>Functionality</h2>
    <ul class="step__list">
      <li class="step__item"><svg><use href="#tick-box"/></svg>Does it work the<br>way you want it to?</li>
      <li class="step__item"><svg><use href="#tick-box"/></svg>Is it what you<br>expected?</li>
    </ul>
  </section>

  <footer class="contact-band">
    <div class="contact-band__corner"></div>
    <p class="contact-band__text contact-band__text--reach">Email us at orders@basaltcreekmetal.com,<br>shoot us a text (555) 204-0187, or<br>reach out via www.basaltcreekmetal.com/contact</p>
    <div class="contact-band__divider"></div>
    <p class="contact-band__text contact-band__text--review"><span class="contact-band__ask">Did we do a good job?</span> If you think so,<br>leave us a review on ReviewPost? If not, Please let us<br>know info@basaltcreekmetal.com or call us 555-476-0192</p>
  </footer>

  <div class="brand-mark">BASALT CREEK METALWORKS</div>
</article>
</body>
</html>
```